Modern Design Business Card industrial maintenance company

Business card design for Company named Brookvale Equipment Services

Target Market(s)

Industrial

Industry/Entity Type

Maintenance and repair

Contact Information for Business Card

Place holder for address, office phone, mobile number and email

Requirements
Must have
• Clean modern look
Nice to have
• N/a

```html
<!DOCTYPE html>
<html lang="en">
<head>
<meta charset="utf-8">
<title>Brookvale Equipment Services — Business Card</title>
<link rel="stylesheet" href="https://fonts.googleapis.com/css2?family=Lato:wght@400;700;900&family=Michroma&display=swap">
<style>
  :root {
    --backdrop: #2b2c2e;
    --card-dark: #232325;
    --card-light: #ffffff;
    --ink: #1a1a1a;
    --ink-soft: #6b6b6b;
    --rule-grey: #9a9a9a;
    --on-dark: #e9e9e9;
    --on-dark-soft: #b8b8b8;
  }
  * { box-sizing: border-box; margin: 0; padding: 0; }
  html, body { width: 1200px; height: 952px; overflow: hidden; }
  body {
    background: var(--backdrop);
    font-family: "Lato", Arial, sans-serif;
    position: relative;
  }
  .card {
    position: absolute;
    width: 560px;
    height: 320px;
    border-radius: 4px;
    box-shadow: 0 18px 40px rgba(0,0,0,.45);
    overflow: hidden;
  }

  /* Back side */
  .card--back {
    left: 90px; top: 540px;
    background: var(--card-dark);
    display: flex; align-items: center; justify-content: center;
  }
  .wordmark { text-align: center; }
  .wordmark__name {
    font-family: "Michroma", Arial, sans-serif;
    font-size: 26px; letter-spacing: 1px;
    color: var(--on-dark);
    line-height: 1.1;
  }
  .wordmark__name--sub { font-size: 12px; letter-spacing: 5px; margin-top: 6px; color: var(--on-dark); }

  /* Front side */
  .card--front {
    left: 560px; top: 110px;
    background: var(--card-light);
  }
  .brand {
    position: absolute; left: 26px; top: 92px; width: 210px;
    display: flex; flex-direction: column; align-items: center; gap: 14px;
  }
  .brand__dot {
    width: 58px; height: 58px; border-radius: 50%;
    border: 3px solid var(--ink);
  }
  .brand__name {
    font-family: "Michroma", Arial, sans-serif;
    font-size: 17px; color: var(--ink); text-align: center; line-height: 1.35;
  }
  .divider { position: absolute; left: 256px; top: 0; width: 14px; height: 320px; }

  .contact { position: absolute; left: 300px; top: 62px; right: 20px; color: var(--ink-soft); }
  .contact__name { font-size: 19px; letter-spacing: .5px; color: #444; }
  .contact__name b { font-weight: 900; color: var(--ink); }
  .contact__title { font-size: 14px; margin-top: 2px; }
  .contact__rule { width: 60px; height: 1px; background: var(--rule-grey); margin: 10px 0 12px; }
  .contact__list { list-style: none; font-size: 13px; line-height: 1.35; }
  .contact__list li { display: flex; gap: 8px; margin-bottom: 6px; }
  .icon {
    flex: none; width: 16px; height: 16px; border-radius: 3px;
    background: var(--ink); display: flex; align-items: center; justify-content: center;
    margin-top: 1px;
  }
  .icon svg { width: 10px; height: 10px; fill: #fff; }
</style>
</head>
<body>

  <section class="card card--front" aria-label="Business card front">
    <div class="brand">
      <span class="brand__dot"></span>
      <span class="brand__name">Brookvale Equipment Services</span>
    </div>

    <svg class="divider" viewBox="0 0 14 320" preserveAspectRatio="none" aria-hidden="true">
      <rect x="6" y="0" width="2" height="200" fill="#9a9a9a"/>
      <polygon points="6,200 8,200 14,214 14,320 3,320 3,208" fill="#1a1a1a"/>
    </svg>

    <div class="contact">
      <p class="contact__name">DANIEL R. <b>WHITMORE</b></p>
      <p class="contact__title">Managing Director</p>
      <div class="contact__rule"></div>
      <ul class="contact__list">
        <li><span class="icon"><svg viewBox="0 0 10 10"><path d="M5 0a3.5 3.5 0 0 0-3.5 3.5C1.5 6 5 10 5 10s3.5-4 3.5-6.5A3.5 3.5 0 0 0 5 0zm0 5a1.4 1.4 0 1 1 0-2.8A1.4 1.4 0 0 1 5 5z"/></svg></span>
          <span>2170 Harbor Ridge Road<br>Portland, OR 97210</span></li>
        <li><span class="icon"><svg viewBox="0 0 10 10"><path d="M2 0l2 2.5-1 1.2a6 6 0 0 0 3.3 3.3l1.2-1L10 8l-1 2C4 10 0 6 0 1z"/></svg></span>
          <span>+00 987 654 32</span></li>
        <li><span class="icon"><svg viewBox="0 0 10 10"><path d="M0 2h10v6H0zM0 2l5 3.5L10 2" stroke="#1a1a1a" stroke-width=".8"/></svg></span>
          <span>info@brookvaleequip.com</span></li>
        <li><span class="icon"><svg viewBox="0 0 10 10"><path d="M2 1l7 3-3 1-1 3z"/></svg></span>
          <span>www.brookvaleequip.com</span></li>
      </ul>
    </div>
  </section>

  <section class="card card--back" aria-label="Business card back">
    <div class="wordmark">
      <p class="wordmark__name">Brookvale</p>
      <p class="wordmark__name wordmark__name--sub">Equipment Services</p>
    </div>
  </section>

</body>
</html>
```